Executive search firm in fashion, luxury and retail industry needs logo and card design.

We are a start-up recruiting firm that specializes in the retail and fashion industry, based in New York. We are looking for something that will appeal to CEO level clients and candidates, but that has a little design edge...not overly corporate but still CEO-appropriate. We have clean, sophisticated taste and want a contemporary feel. Happy to have a two sided card. Not afraid of a little color but it should be high-design, not gimmicky and tasteful.

Quillby Market(s)

CEO's, HR Leaders, in retail, fashion (i.e. Havenmere, Quillby, Otto Vasquel)

Industry/Entity Type

Professional Service

Contact Information for Business Card

Linden Row Talent Partners
Address to be determined
Alder Bay, NY 10990

Marla Tovick
Managing Director
(555)013-2846
mtovick@lindenrowtalent.example

Font styles to use
Serif
Sans Serif

Requirements
Must have
• clean lines, crisp graphics, some color. Prefer a graphic treatment over a "logo" per se. No pictures, etc.
Nice to have
• double sided design.
Should not have
• Gimmicks, smaltz, goop. Think Gallery of Current Forms, not the Pelham Vault. No earth tones, as in beige and brown, no pastels. Strong colors are fine in moderation. Grays are good. Jewel tones are good. No red.

```html
<!DOCTYPE html>
<html lang="en">
<head>
<meta charset="utf-8">
<title>Linden Row Talent Partners — Business Card</title>
<link href="https://fonts.googleapis.com/css2?family=Questrial&display=swap" rel="stylesheet">
<style>
  :root {
    --bg: #e6e7e8;
    --paper: #ffffff;
    --charcoal: #3a3a3c;
    --ink: #1c1c1e;
    --ink-soft: #3d3d40;
    --blue: #1f6fd1;
    --light: #f2f2f2;
    --muted: #a9acb1;
  }
  html, body {
    margin: 0;
    padding: 0;
    width: 1200px;
    height: 1021px;
    overflow: hidden;
    background: var(--bg);
    font-family: "Questrial", "Century Gothic", sans-serif;
  }
  .canvas { position: relative; width: 1200px; height: 1021px; }

  .card {
    position: absolute;
    width: 560px;
    height: 320px;
    box-shadow: 0 14px 30px rgba(0,0,0,.18), 0 2px 4px rgba(0,0,0,.12);
  }
  .card--front { left: 120px; top: 110px; background: var(--paper); }
  .card--back  { left: 520px; top: 450px; background: var(--charcoal); }

  .wordmark { position: absolute; display: flex; align-items: center; gap: 10px; }
  .wordmark__dot { border-radius: 50%; background: var(--blue); flex: none; }
  .wordmark__text { display: flex; flex-direction: column; }
  .wordmark__name { line-height: 1; letter-spacing: -0.5px; white-space: nowrap; }
  .wordmark__sub { text-transform: uppercase; letter-spacing: 0.32em; margin-top: 4px; white-space: nowrap; }

  .card--front .wordmark { left: 40px; top: 168px; }
  .card--front .wordmark__dot { width: 12px; height: 12px; }
  .card--front .wordmark__name { font-size: 26px; color: var(--ink); }
  .card--front .wordmark__sub { font-size: 7px; color: var(--ink-soft); }

  .contact { position: absolute; left: 282px; top: 92px; color: var(--ink); }
  .contact__name { font-size: 24px; margin: 0; font-weight: 400; line-height: 1.2; }
  .contact__title { font-size: 14px; color: var(--blue); margin: 2px 0 14px; }
  .contact__list { list-style: none; margin: 0; padding: 0; font-size: 12.5px; }
  .contact__list li { display: flex; align-items: center; gap: 9px; margin-bottom: 7px; white-space: nowrap; }
  .contact__list svg { width: 13px; height: 13px; flex: none; }
  .icon--fill { fill: var(--blue); }
  .icon--line { fill: none; stroke: var(--blue); stroke-width: 2.4; stroke-linejoin: round; }

  .card--back .wordmark { left: 150px; top: 128px; }
  .card--back .wordmark__dot { width: 16px; height: 16px; }
  .card--back .wordmark__name { font-size: 40px; color: var(--light); }
  .card--back .wordmark__sub { font-size: 9px; color: var(--muted); }
  .accent-line {
    position: absolute; left: 420px; top: 150px;
    width: 140px; height: 3px; background: var(--blue);
  }

  .lockup { left: 60px; top: 850px; gap: 16px; }
  .lockup .wordmark__dot { width: 22px; height: 22px; }
  .lockup .wordmark__name { font-size: 62px; color: var(--ink); }
  .lockup .wordmark__sub { font-size: 15px; color: var(--ink-soft); margin-top: 8px; }
</style>
</head>
<body>
<main class="canvas">

  <section class="card card--front" aria-label="Card front">
    <div class="wordmark">
      <span class="wordmark__dot"></span>
      <div class="wordmark__text">
        <span class="wordmark__name">Linden Row</span>
        <span class="wordmark__sub">Talent Partners</span>
      </div>
    </div>
    <div class="contact">
      <h1 class="contact__name">Marla Tovick</h1>
      <p class="contact__title">Managing Director</p>
      <ul class="contact__list">
        <li>
          <svg class="icon--fill" viewBox="0 0 24 24" aria-hidden="true"><path d="M6.6 10.8a15.1 15.1 0 0 0 6.6 6.6l2.2-2.2a1 1 0 0 1 1-.25 11.4 11.4 0 0 0 3.6.57 1 1 0 0 1 1 1V20a1 1 0 0 1-1 1A17 17 0 0 1 3 4a1 1 0 0 1 1-1h3.5a1 1 0 0 1 1 1c0 1.25.2 2.45.57 3.57a1 1 0 0 1-.25 1z"/></svg>
          (555)013-2846
        </li>
        <li>
          <svg class="icon--line" viewBox="0 0 24 24" aria-hidden="true"><rect x="3" y="5.5" width="18" height="13"/><path d="M3 5.5l9 7 9-7"/></svg>
          mtovick@lindenrowtalent.example
        </li>
        <li>
          <svg class="icon--fill" viewBox="0 0 24 24" aria-hidden="true"><path d="M12 2a7 7 0 0 0-7 7c0 5 7 13 7 13s7-8 7-13a7 7 0 0 0-7-7zm0 9.5A2.5 2.5 0 1 1 12 6.5a2.5 2.5 0 0 1 0 5z"/></svg>
          Alder Bay, NY 10990
        </li>
      </ul>
    </div>
  </section>

  <section class="card card--back" aria-label="Card back">
    <div class="wordmark">
      <span class="wordmark__dot"></span>
      <div class="wordmark__text">
        <span class="wordmark__name">Linden Row</span>
        <span class="wordmark__sub">Talent Partners</span>
      </div>
    </div>
    <span class="accent-line"></span>
  </section>

  <div class="wordmark lockup" aria-label="Linden Row Talent Partners">
    <span class="wordmark__dot"></span>
    <div class="wordmark__text">
      <span class="wordmark__name">Linden Row</span>
      <span class="wordmark__sub">Talent Partners</span>
    </div>
  </div>

</main>
</body>
</html>
```